Website for Healthy Energy Bars

I need the layout for a website that will allow customers to purchase three different energy bars. It should have a slide show of pictures on the front page and the following tabs: About, Nutrition Info, FAQ

The website colors should not conflict with the colors of the company logo. Other than that I am open to design ideas and concepts.

Target Market(s)

Health-Conscious Eaters

Industry/Entity Type

Purchase

Number of Pages Required

3 page

Requirements
Must have
• Logo and pictures of the product
Should not have
• Colors that conflict with the logo colors

```html
<!DOCTYPE html>
<html lang="en">
<head>
<meta charset="utf-8">
<title>Verdabar – Health Energy Nutrition Bars</title>
<link href="https://fonts.googleapis.com/css2?family=Open+Sans:wght@400;600;700&family=Raleway:wght@400;600;700&display=swap" rel="stylesheet">
<style>
:root{
  --green:#6fbf1f;
  --green-dark:#4e9a10;
  --maroon:#7a1630;
  --maroon-dark:#5e0f24;
  --red:#b01e3a;
  --ink:#333;
  --muted:#777;
  --line:#ddd;
  --soft:#f3f3f3;
}
*{margin:0;padding:0;box-sizing:border-box}
html,body{width:784px;height:1200px;overflow:hidden;background:#fff}
body{font-family:"Open Sans",sans-serif;color:var(--ink);font-size:9px;line-height:1.5}
.page{width:784px;height:1200px;position:relative}

/* header */
.site-header{height:73px;position:relative}
.brand{position:absolute;left:62px;top:18px;display:flex;align-items:center;gap:8px}
.brand-dot{width:26px;height:26px;border-radius:50%;background:var(--green)}
.brand-name{font-family:"Raleway",sans-serif;font-weight:700;font-size:26px;color:var(--green-dark)}
.top-links{position:absolute;right:80px;top:10px;font-size:8px;color:var(--muted);display:flex;gap:10px}
.search{position:absolute;right:80px;top:44px;width:130px;height:16px;border:1px solid var(--line);border-radius:2px;font-size:7px;color:#aaa;padding:2px 6px}
.cart{position:absolute;right:62px;top:8px;width:14px;height:12px}

.main-nav{height:26px;background:linear-gradient(#86d02f,var(--green-dark));display:flex;justify-content:center}
.main-nav a{color:#fff;text-decoration:none;font-size:9px;font-weight:600;padding:0 30px;line-height:26px;text-transform:uppercase;border-right:1px solid rgba(255,255,255,.3)}
.main-nav a:first-child{border-left:1px solid rgba(255,255,255,.3)}
.main-nav a.active{background:rgba(255,255,255,.18)}

/* hero */
.hero{height:214px;background:linear-gradient(90deg,#fafafa,#eef0f0);position:relative;border-bottom:1px solid var(--line)}
.hero-copy{position:absolute;left:62px;top:28px;width:280px}
.hero-copy h1{font-family:"Raleway",sans-serif;font-weight:600;font-size:24px;color:#222;line-height:1.15}
.hero-copy h2{font-family:"Raleway",sans-serif;font-weight:600;font-size:15px;color:var(--red);margin:4px 0 8px}
.hero-copy p{font-size:7px;color:var(--muted);width:200px}
.btn{display:inline-block;background:var(--maroon);color:#fff;font-size:8px;padding:4px 12px;border-radius:2px;text-decoration:none}
.hero-copy .btn{margin-top:10px}
.hero-product{position:absolute;left:300px;top:120px;width:110px;height:62px;background:linear-gradient(#f4f1c8,#d8d2a0);border-radius:3px}
.hero-person{position:absolute;left:470px;top:0;width:210px;height:213px;background:linear-gradient(#f1e3dc,#e28aa6)}
.dots{position:absolute;left:62px;bottom:12px;display:flex;gap:4px}
.dots span{width:7px;height:7px;border-radius:50%;background:#bbb}
.dots span:first-child{background:var(--maroon)}

/* welcome */
.welcome{text-align:center;padding:28px 62px 0}
.welcome h2{font-family:"Raleway",sans-serif;font-weight:600;font-size:22px;color:#333;margin-bottom:10px}
.welcome p{font-size:7px;color:var(--muted);margin-bottom:8px}

/* featured */
.featured{position:relative;margin-top:16px;border-top:1px solid var(--line)}
.ribbon{position:absolute;left:50%;top:-12px;transform:translateX(-50%);background:var(--green);color:#fff;font-family:"Raleway",sans-serif;font-weight:600;font-size:12px;padding:4px 42px;border-radius:3px}
.products{display:flex;gap:14px;justify-content:center;padding-top:28px}
.card{width:118px;height:186px;border:1px solid var(--line);text-align:center;background:#fff}
.card-img{height:92px;margin:6px;background:linear-gradient(#f6f4e0,#dcd6a4)}
.card h3{font-size:10px;font-weight:700;margin-top:8px}
.card p{font-size:7px;color:var(--muted)}
.card-foot{display:flex;justify-content:space-between;align-items:center;padding:8px 8px 0}
.price{color:var(--red);font-weight:700;font-size:12px}
.card .btn{font-size:7px;padding:3px 8px}
.arrow{position:absolute;top:100px;width:14px;height:26px}
.arrow.left{left:92px}.arrow.right{right:92px}

/* info */
.info{display:flex;gap:40px;padding:48px 62px 0}
.faq{flex:1}
.info h2{font-family:"Raleway",sans-serif;font-weight:600;font-size:20px;margin-bottom:8px}
.faq h4{font-size:8px;font-weight:600;margin-top:6px}
.faq p{font-size:7px;color:var(--muted)}
.testimonials{width:300px}
.quote{border:1px solid var(--line);padding:12px;display:flex;gap:10px;height:150px}
.avatar{width:46px;height:46px;flex:none;background:linear-gradient(#d8c6b8,#9c8778)}
.quote p{font-size:7px;color:var(--muted)}
.quote .who{margin-top:10px;font-size:7px;font-weight:600;color:var(--ink)}

/* footer */
.site-footer{position:absolute;left:0;top:1030px;width:784px;height:150px;background:var(--maroon);color:#f1d8de;display:flex;gap:40px;padding:18px 62px}
.site-footer h5{font-size:9px;font-weight:700;color:#fff;margin-bottom:6px}
.site-footer li{list-style:none;font-size:7px;line-height:1.7}
.col{width:110px}
.social{display:flex;gap:5px;margin:4px 0 10px}
.social span{width:14px;height:14px;border-radius:50%;background:#d7aab6}
.footer-brand{font-family:"Raleway",sans-serif;font-weight:700;font-size:18px;color:#9ad54a;display:flex;align-items:center;gap:6px}
.footer-brand i{width:16px;height:16px;border-radius:50%;background:#9ad54a}
.cards{display:flex;gap:3px;margin-top:8px}
.cards span{width:18px;height:11px;background:#d7aab6;border-radius:1px}
.bottom-bar{position:absolute;left:0;top:1180px;width:784px;height:20px;background:var(--maroon-dark);color:#cfa9b4;font-size:7px;padding:0 62px;display:flex;justify-content:space-between;align-items:center}
</style>
</head>
<body>
<div class="page">
  <header class="site-header">
    <div class="brand"><span class="brand-dot"></span><span class="brand-name">Verdabar</span></div>
    <div class="top-links"><span>My Account</span><span>Wish List</span><span>Sign Up</span><span>Checkout</span></div>
    <svg class="cart" viewBox="0 0 14 12"><path d="M0 1h3l2 7h7l2-5H4" fill="none" stroke="#666" stroke-width="1.2"/><circle cx="6" cy="10.5" r="1.2" fill="#666"/><circle cx="11" cy="10.5" r="1.2" fill="#666"/></svg>
    <div class="search">Search here</div>
  </header>

  <nav class="main-nav">
    <a href="#" class="active">Home</a><a href="#">About</a><a href="#">Nutrition Bars</a><a href="#">FAQ</a><a href="#">Contact</a>
  </nav>

  <section class="hero">
    <div class="hero-copy">
      <h1>Health Energy Nutrition Bars</h1>
      <h2>Praesent sit amet est dictum dolor</h2>
      <p>Consectetur elit sed do eiusmod tempor incididunt ut labore et dolore magna aliqua, ut enim minim veniam quis.</p>
      <a class="btn" href="#">Order Now</a>
    </div>
    <div class="hero-product" role="img" aria-label="Pack of energy bars"></div>
    <div class="hero-person" role="img" aria-label="Smiling athlete in pink holding an energy bar"></div>
    <div class="dots"><span></span><span></span><span></span><span></span></div>
  </section>

  <section class="welcome">
    <h2>Welcome to Verdabar Mainpage</h2>
    <p>Maecenas tellus lorem dapibus vitae volutpat sed, sollicitudin et nunc. Pellentesque habitant morbi tristique senectus et netus et malesuada fames ac turpis egestas. Nulla facilisi, donec id mauris a erat tincidunt commodo ut eu ligula. Integer consequat, nibh ac placerat porta, massa ante molestie nisl, sit amet volutpat lectus felis nec justo.</p>
    <p>Vivamus mattis purus at velit cursus, vel fermentum magna ultricies. Curabitur ut neque non mi faucibus tempus in vitae erat. Aenean pulvinar ligula at neque aliquet, a vehicula odio lobortis. Suspendisse potenti, in hac habitasse platea dictumst, nullam fringilla velit nec risus.</p>
  </section>

  <section class="featured">
    <div class="ribbon">Featured Products</div>
    <svg class="arrow left" viewBox="0 0 14 26"><path d="M12 2 2 13l10 11" fill="none" stroke="#bbb" stroke-width="2"/></svg>
    <svg class="arrow right" viewBox="0 0 14 26"><path d="M2 2l10 11L2 24" fill="none" stroke="#bbb" stroke-width="2"/></svg>
    <div class="products">
      <div class="card"><div class="card-img" role="img" aria-label="Energy bar product shot"></div><h3>Product Name</h3><p>Short bar description</p><div class="card-foot"><span class="price">$17.18</span><a class="btn" href="#">Add to Cart</a></div></div>
      <div class="card"><div class="card-img" role="img" aria-label="Energy bar product shot"></div><h3>Product Name</h3><p>Short bar description</p><div class="card-foot"><span class="price">$17.18</span><a class="btn" href="#">Add to Cart</a></div></div>
      <div class="card"><div class="card-img" role="img" aria-label="Energy bar product shot"></div><h3>Product Name</h3><p>Short bar description</p><div class="card-foot"><span class="price">$17.18</span><a class="btn" href="#">Add to Cart</a></div></div>
      <div class="card"><div class="card-img" role="img" aria-label="Energy bar product shot"></div><h3>Product Name</h3><p>Short bar description</p><div class="card-foot"><span class="price">$17.18</span><a class="btn" href="#">Add to Cart</a></div></div>
    </div>
  </section>

  <section class="info">
    <div class="faq">
      <h2>FAQ</h2>
      <h4>Maecenas aliquet nibh id turpis</h4>
      <p>Sed tempus lectus ut lorem feugiat, vitae facilisis nibh aliquet. Donec sagittis nunc in dictum placerat, eu porta velit finibus mattis.</p>
      <h4>Praesent sit amet est in dictum</h4>
      <p>Nunc vel arcu id lacus pretium tincidunt. Aliquam erat volutpat, integer bibendum ex vitae magna dignissim, quis viverra nisl porta. Morbi non semper justo, et gravida eros.</p>
    </div>
    <div class="testimonials">
      <h2>Testimonials</h2>
      <div class="quote">
        <div class="avatar" role="img" aria-label="Customer portrait"></div>
        <div>
          <p>Maecenas aliquet nibh id turpis lacinia luctus. Nulla facilisi, quisque eget risus vel mi porta fermentum. Curabitur at odio sed felis tincidunt suscipit in vitae ligula. Integer sodales justo quis lorem tristique, nec dictum neque varius.</p>
          <p class="who">By Jordan Wells<br><span style="font-weight:400;color:#777">Happy customer</span></p>
        </div>
      </div>
    </div>
  </section>

  <footer class="site-footer">
    <div class="col"><h5>COMPANY</h5><ul><li>About Us</li><li>Why Choose</li><li>Meet Team</li><li>Testimonials</li><li>Store Locator</li></ul></div>
    <div class="col"><h5>PRODUCTS</h5><ul><li>Shipping and Delivery</li><li>Payment Methods</li><li>Returns</li><li>Nutrition</li><li>Gift Cards</li></ul></div>
    <div class="col"><h5>SUPPORT</h5><ul><li>FAQs</li><li>Privacy Policy</li><li>Terms and Conditions</li><li>Contact</li></ul>
      <div class="cards"><span></span><span></span><span></span></div></div>
    <div class="col" style="width:160px"><h5>GET IN TOUCH</h5><ul><li>Stay up to date with our news</li></ul>
      <div class="social"><span></span><span></span><span></span><span></span><span></span></div>
      <div class="footer-brand"><i></i>Verdabar</div></div>
  </footer>
  <div class="bottom-bar"><span>© 2014 Verdabar. All rights reserved.</span><span>Top</span></div>
</div>
</body>
</html>
```